KTRWG Promotion Flyer to raise money and communicate our goals

We need a flyer that promotes our organization. We are a 501(c)3 trying to raise money for Arts, Education and Entrepreneurship in our small town.

We promote a social events that improve qualtiy of life and educate people on how to start and expand businesses. Our goal is to make downtown an active and thriving place with many things for people to do and enjoy as well as create a favorable place for business.

Target Market(s)

Wealthy donors and Organizations with cash

Industry/Entity Type

Education

Colors

Designer to choose colors to be used in the design.

Requirements
Must have
• Eye catching graphics and look very professional
• Should appeal to men and women
Nice to have
• Make use of any known psychological colors and fonts etc... that appeal to philanthropic people
Should not have
• Should not be complicated or confusing

```html
<!DOCTYPE html>
<html lang="en">
<head>
<meta charset="utf-8">
<title>KTRWG Membership Flyer</title>
<link href="https://fonts.googleapis.com/css2?family=Lato:wght@400;700&family=Source+Sans+3:wght@700;800&display=swap" rel="stylesheet">
<style>
  :root {
    --page-bg: #e9e6e2;
    --paper: #f6f6f6;
    --blue: #1aa7e0;
    --blue-dark: #0f7fb8;
    --pink: #e6277a;
    --green: #7cbb3b;
    --ink: #222;
    --sky-top: #a9cde8;
    --sky-bottom: #e4eef5;
    --field: #a58f6c;
  }
  * { margin: 0; padding: 0; box-sizing: border-box; }
  html, body { width: 1200px; height: 1200px; overflow: hidden; background: var(--page-bg); }
  .flyer {
    position: absolute; left: 136px; top: 0; width: 928px; height: 1200px;
    background: linear-gradient(#fbfbfb, #eeeeee);
    font-family: "Lato", Arial, sans-serif; color: var(--ink);
  }
  .hero-photo {
    position: absolute; left: 0; top: 0; width: 928px; height: 428px;
    background: linear-gradient(180deg, var(--sky-top) 0%, var(--sky-bottom) 55%, #8c7a5e 78%, var(--field) 100%);
  }
  .brand-badge {
    position: absolute; left: 719px; top: 40px; width: 162px; height: 162px;
    border-radius: 50%; background: #fff; border: 3px solid var(--pink);
    display: flex; align-items: center; justify-content: center;
    font-family: "Lato", Arial, sans-serif; font-weight: 700; font-size: 30px; color: var(--pink);
    letter-spacing: 1px;
  }
  .headline-band {
    position: absolute; left: 0; top: 428px; width: 928px; height: 75px;
    background: rgba(240,240,240,.95);
    display: flex; align-items: center; justify-content: center;
    font-family: "Source Sans 3", Arial, sans-serif; font-weight: 800; font-size: 48px;
    color: var(--blue); letter-spacing: -.3px;
  }
  .headline-band .accent { color: var(--pink); margin-left: 12px; }
  .rule-pink { position: absolute; left: 0; top: 503px; width: 928px; height: 9px; background: var(--pink); border-bottom: 3px solid var(--blue-dark); }
  .intro, .closing {
    position: absolute; left: 44px; width: 840px; font-size: 14.5px; line-height: 18.4px; text-align: justify;
  }
  .intro { top: 563px; }
  .closing { top: 973px; }
  .divider { position: absolute; left: 462px; top: 665px; width: 2px; height: 290px; background: linear-gradient(transparent, #cfcfcf 20%, #cfcfcf 80%, transparent); }
  .feature { position: absolute; width: 392px; }
  .feature-head { position: relative; height: 56px; }
  .feature-icon {
    position: absolute; left: 0; top: 0; width: 56px; height: 56px; border-radius: 50%;
    background: var(--blue-dark); border: 4px solid var(--pink); z-index: 2;
    display: flex; align-items: center; justify-content: center;
  }
  .feature-pill {
    position: absolute; left: 40px; top: 14px; height: 30px; padding: 0 16px 0 26px;
    background: var(--blue); border-radius: 15px; border-bottom: 3px solid var(--pink);
    color: #fff; font-weight: 700; font-size: 16px; line-height: 28px; white-space: nowrap;
    min-width: 162px;
  }
  .feature p { margin-top: 18px; font-size: 14.5px; line-height: 18.4px; text-align: justify; }
  .f-promote { left: 44px; top: 710px; }
  .f-help { left: 492px; top: 710px; }
  .f-provide { left: 44px; top: 851px; }
  .f-work { left: 492px; top: 851px; }
  .rule-blue { position: absolute; left: 0; top: 1121px; width: 928px; height: 4px; background: var(--blue); }
  .footer {
    position: absolute; left: 0; top: 1133px; width: 928px; height: 67px; background: var(--green);
    display: flex; align-items: center; justify-content: center;
    font-size: 17px; letter-spacing: 3px; color: #1e2a10;
  }
</style>
</head>
<body>
<main class="flyer">
  <div class="hero-photo" role="img" aria-label="Photograph of the town's open-sided red and cream pavilion under a blue sky"></div>
  <div class="brand-badge">KTRWG</div>

  <h1 class="headline-band">We enter by<span class="accent">YOUR GRACE</span></h1>
  <div class="rule-pink"></div>

  <p class="intro">The Millbrook Small Business Association (KTRWG) is a local leader in the areas of Arts, Education and Entrepreneurship and is working diligently to promote Millbrook and revitalize our downtown. When you become an KTRWG Member, you will be a part of the citywide work that the KTRWG does every day to improve the lives of citizens of Millbrook:</p>

  <div class="divider"></div>

  <section class="feature f-promote">
    <div class="feature-head">
      <div class="feature-icon">
        <svg width="26" height="34" viewBox="0 0 26 34" fill="none" stroke="#fff" stroke-width="1.6"><path d="M13 2c5 5 5 14 3 20h-6C8 16 8 7 13 2z"/><circle cx="13" cy="12" r="2.5"/><path d="M10 22l-4 5 3-1M16 22l4 5-3-1M13 25v6"/></svg>
      </div>
      <div class="feature-pill">WE PROMOTE</div>
    </div>
    <p>Millbrook Hotels, Shopping and Events that make Millbrook a pleasant, exciting and prosperous place to live.</p>
  </section>

  <section class="feature f-help">
    <div class="feature-head">
      <div class="feature-icon">
        <svg width="30" height="30" viewBox="0 0 30 30" fill="none" stroke="#fff" stroke-width="2" stroke-linecap="round"><circle cx="20" cy="6" r="2.5" fill="#fff"/><path d="M20 9l-3 8 4 5M17 17l-5 2M8 10l4 3"/><path d="M4 28h22"/></svg>
      </div>
      <div class="feature-pill">WE HELP</div>
    </div>
    <p>entrepreneur's start and grow their businesses in a tax efficient and appropriate way.</p>
  </section>

  <section class="feature f-provide">
    <div class="feature-head">
      <div class="feature-icon">
        <svg width="32" height="32" viewBox="0 0 32 32" fill="none" stroke="#fff" stroke-width="1.6"><circle cx="16" cy="16" r="5"/><path d="M16 3v8M16 21v8M3 16h8M21 16h8M7 7l5.5 5.5M19.5 19.5L25 25M25 7l-5.5 5.5M12.5 19.5L7 25"/></svg>
      </div>
      <div class="feature-pill">WE PROVIDE</div>
    </div>
    <p>training and resources to anyone interested Arts, Education and Entrepreneurship.</p>
  </section>

  <section class="feature f-work">
    <div class="feature-head">
      <div class="feature-icon">
        <svg width="32" height="32" viewBox="0 0 32 32" fill="none" stroke="#fff" stroke-width="1.6"><circle cx="16" cy="6" r="2.5"/><circle cx="6" cy="16" r="2.5"/><circle cx="16" cy="16" r="2.5"/><circle cx="26" cy="16" r="2.5"/><circle cx="16" cy="26" r="2.5"/><path d="M9 16h4M19 16h4M16 9v4M16 19v4"/></svg>
      </div>
      <div class="feature-pill">WE WORK</div>
    </div>
    <p>with all levels of local government to promote our community and create a fertile environment for growth.</p>
  </section>

  <p class="closing">Every day, we look for ways to help our local businesses grow and expand, but we need you by our side. As an KTRWG Member, you can help provide training, education and support, and you can give our many businesses a chance to grow and our citizens the opportunity to experience big town amenities and events in a small town. Members' regular monthly gifts provide a consistent, reliable income stream that allows us to spend less time fundraising—and more time helping our businesses and community. Becoming an KTRWG Member is an easy, efficient and tax-deductible way to make a difference for our community all year long. Please donate today.</p>

  <div class="rule-blue"></div>
  <footer class="footer">www.millbrookbuzz.org</footer>
</main>
</body>
</html>
```